Webdesign für Brenner Flusstrom
Zielgruppe
Ansprechpartner für Planung und Errichtung von Stromerzeugung durch erneuerbare Energien. Alle Interessen im privaten, teilöffentlichen und öffentlichen Bereich, die mittel- und langfristig umweltschonenden Strom nutzen wollen.
Aufgabenstellung
- Farben bitte in den Unternehmensfarben Blau/Weiß mit einem kleinen Anteil Orange
- Bilder nach Möglichkeit bitte nur eigene (siehe Anhang)
- klare und übersichtliche Struktur
- KEIN Abklatsch der alten Webseite

```html
<!DOCTYPE html>
<html lang="de">
<head>
<meta charset="utf-8">
<title>Brenner Flusstrom – Home</title>
<link href="https://fonts.googleapis.com/css2?family=Open+Sans:wght@300;400;600;700&display=swap" rel="stylesheet">
<style>
:root{
  --navy:#00007f;
  --sky:#7aa7ff;
  --orange:#ff8c00;
  --grey-bg:#f0f0f0;
  --text:#4a4a4a;
  --footer:#444444;
  --white:#ffffff;
}
*{box-sizing:border-box;margin:0;padding:0}
html,body{width:923px;height:1200px;overflow:hidden}
body{font-family:"Open Sans",sans-serif;background:var(--white);color:var(--text);position:relative}
.site-header{position:absolute;top:0;left:0;width:923px;height:56px;background:var(--navy)}
.brand-small{position:absolute;left:71px;top:15px;width:60px;color:var(--white);font-weight:700;font-size:10px;line-height:12px}
.main-nav a,.meta-nav a{position:absolute;color:var(--white);font-weight:700;font-size:10px;text-decoration:none;line-height:20px}
.main-nav .active{left:184px;top:21px;width:59px;height:20px;border-radius:10px;background:var(--sky);text-align:center}
.caret{font-size:7px;margin-left:8px}
.hero{position:absolute;top:56px;left:0;width:923px;height:273px;
  background:linear-gradient(90deg,#6b6a63 0%,#a9aea8 25%,#c89a74 45%,#d9a17a 55%,#8f7d66 80%,#5a5549 100%)}
.hero-shade{position:absolute;inset:0;background:linear-gradient(180deg,rgba(255,255,255,.15),rgba(60,30,20,.25))}
.hero-brand{position:absolute;left:69px;top:125px;width:100px;height:100px;border-radius:50%;background:var(--white);
  display:flex;align-items:center;justify-content:center;text-align:center;color:var(--navy);font-weight:700;font-size:13px;line-height:16px}
.hero-title{position:absolute;left:200px;top:124px;color:var(--white);font-size:21px;line-height:29px;font-weight:700}
.hero-title span{font-weight:300;display:block}
.career-badge{position:absolute;left:731px;top:33px;width:110px;height:110px;border-radius:50%;background:var(--orange);
  display:flex;align-items:center;justify-content:center}
.career-badge p{transform:rotate(15deg);color:var(--white);font-weight:700;font-size:13px;line-height:15px;text-align:center;width:96px}
.partner{position:absolute;left:731px;top:226px;display:flex;align-items:center;color:var(--white);font-size:10px;line-height:13px}
.partner-mark{width:14px;height:14px;background:var(--white);margin:0 10px 0 10px}
.partner-text{border-left:1px solid var(--white);padding-left:6px}
.services{position:absolute;top:329px;left:0;width:923px;height:499px;background:var(--grey-bg)}
.section-title{position:absolute;left:67px;font-size:18px;font-weight:400;color:var(--text)}
.services .section-title{top:22px}
.card{position:absolute;top:65px;width:258px;height:395px;background:var(--white);border-radius:10px;overflow:hidden;box-shadow:0 2px 6px rgba(0,0,0,.12)}
.card-photo{height:158px}
.card h3{display:flex;align-items:center;gap:6px;margin:16px 0 0 17px;color:var(--navy);font-size:19px;font-weight:700}
.card p{margin:12px 16px 0 17px;font-size:9.6px;line-height:13px}
.card p+p{margin-top:13px}
.btn-more{position:absolute;left:16px;right:15px;top:352px;height:26px;border-radius:13px;background:var(--navy);color:var(--white);
  font-weight:700;font-size:10px;line-height:26px;text-align:center;text-decoration:none}
.career .section-title{top:860px}
.career-box{position:absolute;left:67px;top:911px;width:789px;height:194px;background:var(--navy);border-radius:12px;text-align:center}
.career-box h2{margin:35px 50px 0;color:var(--white);font-size:17.5px;line-height:24.5px;font-weight:700}
.career-actions{margin-top:17px;display:flex;justify-content:center;gap:13px}
.career-actions a{width:120px;height:26px;border-radius:13px;font-weight:700;font-size:10px;line-height:26px;text-decoration:none}
.btn-light{background:var(--white);color:var(--navy)}
.btn-sky{background:var(--sky);color:var(--white)}
.site-footer{position:absolute;top:1148px;left:0;width:923px;height:52px;background:var(--footer)}
.legal a{position:absolute;top:18px;color:var(--white);font-weight:700;font-size:10px;text-decoration:none}
.mail{position:absolute;left:675px;top:18px;width:176px;height:20px;border-radius:10px;background:var(--sky);color:var(--white);
  font-weight:700;font-size:10px;line-height:20px;text-align:center;text-decoration:none}
</style>
</head>
<body>
<header class="site-header">
  <div class="brand-small">Brenner Flusstrom</div>
  <nav class="main-nav">
    <a class="active" href="#">Home</a>
    <a style="left:268px;top:21px" href="#">Unternehmen</a>
    <a style="left:376px;top:21px" href="#">Leistungen<span class="caret">▼</span></a>
    <a style="left:484px;top:21px" href="#">Referenzen</a>
  </nav>
  <nav class="meta-nav">
    <a style="left:723px;top:19px" href="#">Hilfe &amp; Kontakt</a>
    <a style="left:816px;top:19px" href="#">Karriere</a>
  </nav>
</header>

<section class="hero">
  <div class="hero-shade" role="img" aria-label="Lachende junge Frau mit wehendem Haar vor Windrädern auf einem Feld"></div>
  <div class="hero-brand">Brenner<br>Flusstrom</div>
  <h1 class="hero-title"><span>Neue Energie?</span>Lass uns das<br>gemeinsam machen.</h1>
  <div class="career-badge"><p>Starte jetzt deine Karriere bei BRENNER Flusstrom</p></div>
  <div class="partner"><div class="partner-mark"></div><div class="partner-text">Premiumpartner<br>von Solvanta</div></div>
</section>

<section class="services">
  <h2 class="section-title">Unsere Leistungen von Brenner</h2>

  <article class="card" style="left:67px">
    <div class="card-photo" role="img" aria-label="Wasserkraftwerk aus Holz an einem Wehr im grünen Flusstal" style="background:linear-gradient(160deg,#6f8a4e,#3f5a35 50%,#8c9486)"></div>
    <h3><svg width="26" height="22" viewBox="0 0 26 22" fill="none" stroke="#00007f" stroke-width="1.2"><path d="M2 4h22M3 4v13M23 4v13M7 8v9M12 8v9M17 8v9M2 17h22M3 20c2-1.5 4 1.5 6 0s4 1.5 6 0 4 1.5 6 0"/></svg>Wasserkraftanlagen</h3>
    <p>Wir haben uns auf die elektrotechnische und hydraulische Ausstattung von Wasserkraftanlagen spezialisiert.</p>
    <p>In unseren Steuerungen verwenden wir durchgängig Komponenten deutscher Hersteller und können mit einer sehr guten Ersatzteilverfügbarkeit im Fehlerfall schnelle Abhilfe schaffen.</p>
    <a class="btn-more" href="#">Mehr erfahren</a>
  </article>

  <article class="card" style="left:333px">
    <div class="card-photo" role="img" aria-label="Monteur installiert Solarmodule auf einem großen Hallendach" style="background:linear-gradient(180deg,#7ea3c9,#b9c9d6 45%,#9aa4ad)"></div>
    <h3><svg width="28" height="26" viewBox="0 0 28 26" fill="none" stroke="#00007f" stroke-width="1.1"><path d="M2 10h18l-3 10H-1zM7 10l-3 10M12 10l-3 10M17 10l-3 10M1 15h18M9 20v4M5 24h8"/><circle cx="23" cy="5" r="2.5"/><path d="M23 0v1M23 9v1M18 5h1M27 5h1"/></svg>Photovoltaik</h3>
    <p>Unsere Ingenieure und Meister planen Ihre Photovoltaikanlage individuell nach den Gegebenheiten vor Ort in Enger Zusammenarbeit mit Statikern und Brandschutz.</p>
    <p>Die Installation erfolgt durch unsere Monteure mit langjähriger Erfahrung im Industriebau auf höchstem handwerklichem Niveau.</p>
    <a class="btn-more" href="#">Mehr erfahren</a>
  </article>

  <article class="card" style="left:598px">
    <div class="card-photo" role="img" aria-label="Rotes Elektroauto an einer Ladesäule im Grünen" style="background:linear-gradient(120deg,#6d8a5a,#9aae7e 45%,#b3403a 75%,#7b9366)"></div>
    <h3><svg width="22" height="22" viewBox="0 0 22 22" fill="none" stroke="#00007f" stroke-width="1.3"><circle cx="11" cy="11" r="9.5"/><path d="M9 7v3M13 7v3M8 10h6v2a3 3 0 0 1-6 0zM11 15v3"/></svg>Mobilität</h3>
    <p>Ein Elektrofahzeug probefahren, die geräuschlose Beschleunigung genießen und den WOW! - Effekt erleben. Sprechen Sie uns an, wir setzen Ihre Wünsche um.</p>
    <p>Ob Probefahrt, Wochenendmiete oder Langzeitmiete - mit uns sind Sie in der neuen Mobilität angekommen!</p>
    <a class="btn-more" href="#">Mehr erfahren</a>
  </article>
</section>

<section class="career">
  <h2 class="section-title">Beste Aussichten – jetzt bewerben und durchstarten!</h2>
  <div class="career-box">
    <h2>Arbeiten Sie für die Stadt, die Sie lieben. Wir sind einer der größten Arbeitgeber der Stadt und bieten interessierten Bewerbern ein attraktives Arbeitsumfeld – vom Job-Einsteiger bis zum langjährigen Profi.</h2>
    <div class="career-actions">
      <a class="btn-light" href="#">Stellenangebote</a>
      <a class="btn-sky" href="#">Initiativbewerbung</a>
    </div>
  </div>
</section>

<footer class="site-footer">
  <nav class="legal">
    <a style="left:77px" href="#">Impressum</a>
    <a style="left:141px" href="#">Datenschutz</a>
    <a style="left:211px" href="#">Sitemap</a>
  </nav>
  <a class="mail" href="#">info(at)energietechnik-brenner.de</a>
</footer>
</body>
</html>
```